Corporate Letter head and Pagecraft Writer Template

Brief
Design three clean, modern, professional corporate letter templates that include the Brightwell Corporation word-mark logo, company name and address and url. The designs should use one or more but no more than three tints/shades from our corporate colour pallet.
Templates should be produced in A4 and Letter formats as a Writer file and should use Helvetica Now Display as the embedded font.
Design Preference:
Colour block designs, solid borders with flowing smooth lines, single side borders with connected header and footer, cut off or half page headers and footers are all acceptable.
Deliverables are:
1. Three graphic design files one for each brand logo colour and design
2. Three Writer templates in 2 formats A4 and Letter
Enclosed are:
1. Three word mark logos with reverse versions of each, one for each primary brand colour.
2. Brightwell corporate colour pallet
3. Brightwell address and url
4. Helvetica Now Display font files

Target Market(s)

Professional Letter Writing to Suppliers, Customers and Authorities

Industry/Entity Type

High Tech

Font styles to use
Sans Serif
Other font styles liked:
• Helvetica Now Display

Requirements
Must have
• Clean, modern and effective design incorporating Brightwell Wordmark logo

```html
<!DOCTYPE html>
<html lang="en">
<head>
<meta charset="UTF-8">
<title>Brightwell Corporation Letterhead</title>
<link href="https://fonts.googleapis.com/css2?family=Inter:wght@400;600;700;800&display=swap" rel="stylesheet">
<style>
  :root {
    --brand-blue: #1ba1de;
    --brand-blue-dark: #1387c0;
    --brand-orange: #f1592a;
    --ink: #2b2b2b;
    --rule: #3aa6dc;
    --paper: #ffffff;
    --pattern-tint: #eef2f6;
  }
  * { margin: 0; padding: 0; box-sizing: border-box; }
  html, body { width: 865px; height: 1200px; overflow: hidden; background: var(--paper); }
  .letterhead {
    position: relative;
    width: 865px;
    height: 1200px;
    background: var(--paper);
    font-family: "Inter", Helvetica, Arial, sans-serif;
    color: var(--ink);
    overflow: hidden;
  }
  .frame-shapes { position: absolute; inset: 0; }
  .wordmark {
    position: absolute;
    left: 52px;
    top: 30px;
    font-size: 44px;
    font-weight: 800;
    letter-spacing: -1px;
    color: #ffffff;
  }
  .web-address {
    position: absolute;
    right: 58px;
    top: 44px;
    font-size: 21px;
    font-weight: 700;
    color: #ffffff;
  }
  .header-pattern {
    position: absolute;
    left: 560px;
    top: 82px;
    width: 305px;
    height: 110px;
    background: linear-gradient(100deg, rgba(238,242,246,0) 0%, var(--pattern-tint) 55%, #e4eaf0 100%);
  }
  .header-rule {
    position: absolute;
    left: 296px;
    top: 244px;
    width: 370px;
    height: 2px;
    background: var(--rule);
  }
  .letter-body {
    position: absolute;
    left: 107px;
    top: 370px;
    width: 650px;
    font-size: 14.5px;
    line-height: 19px;
  }
  .letter-body p { margin-bottom: 19px; }
  .sign-off {
    position: absolute;
    right: 108px;
    top: 952px;
    text-align: right;
  }
  .signer-name { font-size: 19px; font-weight: 700; }
  .signer-role { font-size: 12px; margin-top: 2px; }
  .signature {
    position: absolute;
    left: 505px;
    top: 1010px;
    width: 245px;
    height: 62px;
    background: linear-gradient(90deg, rgba(40,40,40,0.06), rgba(40,40,40,0.14), rgba(40,40,40,0.06));
    border-radius: 30px;
  }
  .company-address {
    position: absolute;
    left: 282px;
    top: 1127px;
    width: 520px;
    font-size: 15px;
    line-height: 20px;
    color: #ffffff;
  }
</style>
</head>
<body>
<div class="letterhead">
  <svg class="frame-shapes" width="865" height="1200" viewBox="0 0 865 1200" aria-hidden="true">
    <!-- header -->
    <rect x="330" y="0" width="535" height="12" fill="var(--brand-blue)"/>
    <polygon points="0,0 340,0 300,115 0,115" fill="var(--brand-blue)"/>
    <polygon points="350,28 865,28 865,80 330,80" fill="var(--brand-orange)"/>
    <polygon points="0,115 300,115 292,140 0,140" fill="var(--brand-blue-dark)" opacity="0.35"/>
    <!-- footer -->
    <polygon points="0,940 150,1200 0,1200" fill="var(--brand-blue)"/>
    <polygon points="0,1010 110,1200 60,1200 0,1100" fill="var(--brand-blue-dark)"/>
    <polygon points="0,1040 200,1108 240,1200 170,1200" fill="var(--brand-blue)" opacity="0.9"/>
    <polygon points="220,1108 865,1108 865,1185 250,1185" fill="var(--brand-orange)"/>
    <polygon points="230,1185 865,1185 865,1200 236,1200" fill="var(--brand-blue)"/>
  </svg>

  <div class="wordmark">Brightwell</div>
  <div class="web-address">www.brightwell-corp.com</div>
  <div class="header-pattern" role="img" aria-label="Faint geometric triangle pattern"></div>
  <div class="header-rule"></div>

  <div class="letter-body">
    <p>Dear Sir/Madam,</p>
    <p>Lorem ipsum dolor sit amet, consectetuer adipiscing elit, sed diam nonummy nibh euismod tincidunt ut laoreet dolore magna aliquam erat volutpat. Ut wisi enim ad minim veniam, quis nostrud exerci tation ullamcorper suscipit lobortis nisl ut aliquip ex ea commodo consequat. Duis autem vel eum iriure dolor in hendrerit in vulputate velit esse molestie consequat, vel illum dolore eu feugiat nulla facilisis</p>
    <p>at vero eros et accumsan et iusto odio dignissim qui blandit praesent luptatum zzril delenit augue duis dolore te feugait nulla facilisi. Lorem ipsum dolor sit amet, cons ectetuer adipiscing elit, sed diam nonummy nibh euismod tincidunt ut laoreet dolore magna aliquam erat volutpat.</p>
    <p>Ut wisi enim ad minim veniam, quis nostrud exerci tation ullamcorper suscipit lobortis nisl ut aliquip ex ea commodo consequat. Lorem ipsum dolor sit amet, consectetuer adipiscing elit, sed diam nonummy nibh euismod</p>
  </div>

  <div class="sign-off">
    <div class="signer-name">Daniel Harper</div>
    <div class="signer-role">Account Manager</div>
  </div>
  <div class="signature" role="img" aria-label="Handwritten signature of Daniel Harper"></div>

  <div class="company-address">Brightwell Corporation 4820 NW Cedar Ridge Drive,<br>Suite 210, Lakeview, OR 97630 United States</div>
</div>
</body>
</html>
```